New Website for Belcourt Manor at www.belcourt.com.au

A new logo has been designed (through pixel forge) and we now want to align the look and feel of our website at www.belcourt.com.au to the new logo. The content and page names (e.g. Grounds) will remain largely unchanged for the new site, so please submit a new look "Home" page, using our new logo, current text and any photos you choose from the existing gallery at our website. I have also attached the current "Home" page photos.

Industry/Entity Type

Accommodation

Number of Pages Required

1 page

Requirements
Must have
• Logo to be presented on white background.

```html
<!DOCTYPE html>
<html lang="en">
<head>
<meta charset="utf-8">
<title>Belcourt Manor – Home</title>
<link rel="stylesheet" href="https://fonts.googleapis.com/css2?family=Raleway:wght@400;500;600;700&display=swap">
<style>
:root{
  --blue:#0a9ad9;
  --blue-dark:#0b7fc0;
  --blue-light:#2fb4ee;
  --text:#5a5a5a;
  --muted:#777;
  --panel:#ebebeb;
  --footer:#262626;
  --footer-text:#d8d8d8;
  --white:#fff;
}
*{box-sizing:border-box;margin:0;padding:0}
html,body{width:893px;height:1200px;overflow:hidden;background:var(--white)}
body{font-family:'Raleway',sans-serif;color:var(--text);position:relative}
.site-header{position:absolute;left:0;top:0;width:893px;height:72px;background:var(--white)}
.brand{position:absolute;left:74px;top:20px;display:flex;align-items:center;gap:8px;color:var(--blue);font-weight:600;font-size:22px;letter-spacing:.3px}
.brand-dot{width:14px;height:14px;border-radius:50%;background:#f5c330}
.social-top{position:absolute;left:560px;top:30px;display:flex;gap:10px}
.social-top span{width:18px;height:18px;display:block;border-radius:2px}
.search{position:absolute;left:680px;top:22px;width:140px;height:33px;border:1px solid #e4e4e4;display:flex}
.search-field{flex:1;font-size:10px;color:#aaa;padding:11px 0 0 8px}
.search-btn{width:36px;height:31px;background:var(--blue);display:flex;align-items:center;justify-content:center}
.main-nav{position:absolute;left:0;top:72px;width:893px;height:42px;background:linear-gradient(var(--blue-light),var(--blue-dark));display:flex;padding-left:62px}
.main-nav a{color:var(--white);text-decoration:none;font-size:9.6px;font-weight:600;line-height:42px;padding:0 13px;position:relative;letter-spacing:.2px}
.main-nav a + a::before{content:"";position:absolute;left:0;top:16px;height:10px;border-left:1px solid rgba(255,255,255,.35)}
.main-nav a.active{background:rgba(0,60,120,.25)}
.hero{position:absolute;left:0;top:114px;width:893px;height:340px;background:linear-gradient(#4a7a3a 0%,#d94a2a 30%,#e8c35a 55%,#9a8f80 85%,#4d6a3a 100%);box-shadow:0 10px 14px -8px rgba(0,0,0,.35)}
.hero-arrow{position:absolute;top:155px}
.intro{position:absolute;left:0;top:488px;width:893px;text-align:center}
.intro h1{color:var(--blue);font-size:15px;font-weight:500;letter-spacing:.2px}
.intro p{margin:22px auto 0;width:640px;font-size:8.8px;line-height:19.2px;color:var(--text)}
.room{position:absolute;top:636px;width:358px;height:338px;background:var(--panel);box-shadow:0 8px 10px -6px rgba(0,0,0,.3)}
.room-head{height:60px;background:var(--blue);color:var(--white);text-align:center;padding-top:12px}
.room-head h2{font-size:13.5px;font-weight:500}
.room-head p{font-size:10.5px;font-weight:600;margin-top:6px}
.room-photo{height:202px}
.room-facts{position:absolute;left:16px;top:276px;display:grid;grid-template-columns:110px 110px;row-gap:14px;font-size:9px;color:var(--muted)}
.room-facts span{display:flex;align-items:center;gap:8px}
.fact-icon{width:14px;height:8px;background:#8a8a8a;border-radius:1px}
.price{position:absolute;right:14px;top:286px;background:var(--blue);color:var(--white);font-size:10.5px;padding:7px 6px}
.site-footer{position:absolute;left:0;top:1009px;width:893px;height:191px;background:var(--footer)}
.social-foot{position:absolute;left:344px;top:37px;display:flex;gap:21px}
.social-foot span{width:38px;height:38px;border:2px solid var(--white);border-radius:50%}
.foot-rule{position:absolute;left:360px;top:89px;width:174px;border-top:2px solid #444}
.foot-nav{position:absolute;left:0;top:117px;width:893px;text-align:center;font-size:9.6px;font-weight:500;color:var(--footer-text)}
.foot-nav a{color:inherit;text-decoration:none}
.foot-nav i{font-style:normal;margin:0 9px;color:#888}
.copyright{position:absolute;left:0;top:151px;width:893px;text-align:center;font-size:8.8px;color:var(--footer-text)}
</style>
</head>
<body>
<header class="site-header">
  <div class="brand"><span class="brand-dot"></span>Belcourt Manor</div>
  <div class="social-top">
    <span style="background:#3b5a99"></span><span style="background:#2aa3e0"></span><span style="background:#f28a21"></span><span style="background:#d8432f"></span>
  </div>
  <div class="search"><div class="search-field">search here</div><div class="search-btn">
    <svg width="16" height="16" viewBox="0 0 16 16"><circle cx="6" cy="6" r="4.2" fill="none" stroke="#fff" stroke-width="2"/><line x1="9" y1="9" x2="14" y2="14" stroke="#fff" stroke-width="2.6" stroke-linecap="round"/></svg>
  </div></div>
</header>
<nav class="main-nav">
  <a class="active">Main</a><a>Mansion</a><a>Bedrooms</a><a>Options</a><a>Fox and Hare</a><a>Grounds</a><a>Location</a><a>Gallery</a><a>Contact</a><a>Availability</a><a>DIY Weddings</a>
</nav>
<div class="hero" role="img" aria-label="Aerial photo of the yellow manor with red tiled roofs, arched walkway and gardens">
  <svg class="hero-arrow" style="left:31px" width="12" height="18" viewBox="0 0 12 18"><polyline points="9,2 3,9 9,16" fill="none" stroke="#fff" stroke-width="2"/></svg>
  <svg class="hero-arrow" style="left:848px" width="12" height="18" viewBox="0 0 12 18"><polyline points="3,2 9,9 3,16" fill="none" stroke="#fff" stroke-width="2"/></svg>
</div>
<section class="intro">
  <h1>PALATIAL ESTATE AND LUXURY RESORT</h1>
  <p>On over 2 manicured garden acres, Belcourt Manor is a unique Gold Coast estate, centrally located in the prestigious rural suburb of Wyndale. More about our Location The estate features a grand mansion, private pub (The Fox and Hare), sparkling resort pool, tennis court and playground. Magnificent properties rarely feel so warm and welcoming – so browse away and visit our photo gallery – and we look forward to having you stay as our guests.<br>For prices, availability and guest reviews</p>
</section>
<article class="room" style="left:74px">
  <div class="room-head"><h2>King (Master) Suite</h2><p>Sleeps 4 | King bed | Double sofa bed</p></div>
  <div class="room-photo" role="img" aria-label="Aerial photo of the manor with pool and palm trees" style="background:linear-gradient(160deg,#c85a3a,#3f6a32 45%,#3aa7c0 65%,#2f4a28)"></div>
  <div class="room-facts"><span><b class="fact-icon"></b>( 4 ) Bed Rooms</span><span><b class="fact-icon"></b>( 6 ) Sleeps</span><span><b class="fact-icon"></b>( 3 ) King bed</span><span><b class="fact-icon"></b>( 10 ) Double Sofa</span></div>
  <div class="price">$ 4699 / - Month</div>
</article>
<article class="room" style="left:461px">
  <div class="room-head"><h2>King (Master) Suite</h2><p>Sleeps 4 | King bed | Double sofa bed</p></div>
  <div class="room-photo" role="img" aria-label="Photo of the lounge with leather sofas, fireplace and gallery balcony" style="background:linear-gradient(#e9e4da,#d8cbb8 55%,#a8744a 80%,#3a3a3a)"></div>
  <div class="room-facts"><span><b class="fact-icon"></b>( 5 ) Bed Rooms</span><span><b class="fact-icon"></b>( 5 ) Sleeps</span><span><b class="fact-icon"></b>( 6 ) King bed</span><span><b class="fact-icon"></b>( 2 ) Double Sofa</span></div>
  <div class="price">$ 5000 / - Month</div>
</article>
<footer class="site-footer">
  <div class="social-foot"><span></span><span></span><span></span><span></span></div>
  <div class="foot-rule"></div>
  <nav class="foot-nav"><a>Main</a><i>•</i><a>Mansion</a><i>•</i><a>Bedrooms</a><i>•</i><a>Options</a><i>•</i><a>Fox and Hare</a><i>•</i><a>Grounds</a><i>•</i><a>Location</a><i>•</i><a>Gallery</a><i>•</i><a>Contact</a><i>•</i><a>Availability</a><i>•</i><a>DIY Weddings</a></nav>
  <div class="copyright">All Rights Reserved . copyrights2016@belcourt.com.au</div>
</footer>
</body>
</html>
```